BrookVale Care - Figma **Updated**

Below are the instructions for the website redesign project for BrookVale Care:
Website Design Review
• Color Scheme: Maintain the clean and professional Red and White color theme.
• Layout: Ensure the layout is straightforward and user-friendly.
• Typography: Use modern and easy-to-read font choices.
• Mobile Optimization: Ensure the website is fully optimized for mobile devices.
Design Requirements
• Clean, Minimalistic, and Responsive Design:
o The design should be clean, easy to navigate, and modern.
o The primary user base consists of seniors, so accessibility and simplicity are key.
• Location-Based Pages:
o Develop pages for each medical clinic and pharmacy location to provide a unique digital presence for each branch.
• Current Content:
o The current content is good but needs to be more efficient and user-friendly for patients.
• Doctor and Staff Introductions:
o Include an introduction section for our doctors and staff to build trust with visitors.
• Custom Design:
o Please avoid using ready-made themes. The preferred design source is a Figma file for development with Elementor.
• Logo:
o See the attached logo for reference.
Key Sections to Enhance
• My Team Section: Enhance this section to highlight healthcare professionals and build trust with visitors.
• Footer Section: Improve the footer by including more links to important sections and social media icons. Ensure the DosaTrak Logo is included on all footers.
• Contact Us Page: Enhance the Contact Us page to include options to upload documents and select specific locations or services.
• Intake Form Page: Improve the Intake Form page by implementing user-friendly and accessible forms.
• Patient Consent Forms: Implement patient consent forms for marketing purposes that are integrated with our database and software.
Websites for Design Inspiration
1. Pelvo Wellness: https://www.pelvowellness.example/?form=MG0AV3
• What We Like: The overall theme, font choices, and the look and feel of the website.
2. TabletNest: https://www.tabletnest.example/
• What We Like: The clean and intuitive layout.
3. Orvanta Care: https://orvantacare.example/
• What We Like: Everything about the design, including aesthetics, usability, and functionality.

Color and Theme Ideas
• Clinic Red, Pharmacy Green, Blue Branding:
o https://www.pelvowellness.example/?form=MG0AV3
o https://quorvix.example/
o https://www.kfl.example/en/financing?form=MG0AV3
o https://remotejourneycare.example/
Design Inspirations
• https://orvantacare.example/
• https://www.tabletnest.example/
• https://www.plinths.example/online/pharmacy/
• https://pharmacy.zentoro.example/
• https://www.dosecrate.example/how-it-works
• https://farcareqo.example/
Pages to Design
1. Landing Page (Clinic): https://brookvalecare.ca/
2. Medical Clinic Intake Instructions: https://brookvalecare.ca/medical-clinic-intake-form/
3. My Team Page and Introduction for Each Team Member
4. Book Appointment: https://brookvalecare.ca/book-appointment/
o Dropdown/Options on the page:
1. Family Practice
2. Walk-In Telehealth
3. Travel Consultation – Telehealth
4. Private Consult with Nurse Practitioner
5. Pharmacy: https://brookvalecare.ca/pharmacy/ (Pay attention to Pop-up Design)
6. Home Monitoring: https://brookvalecare.ca/home-monitoring-program/
7. Home Health Care: https://brookvalecare.ca/home-healthcare/
8. Contact Us: https://brookvalecare.ca/contact/
9. Resources: https://brookvalecare.ca/resources/ (We need Blog and News)
10. Blog Template: https://brookvalecare.ca/2025/02/14/find-doctor-surrey/ (Need massive improvement and responsiveness)
11. Join My Team: https://brookvalecare.ca/career/
Additional Improvements
• Header, Footer, and Banners: Massive improvement needed (Video integration would be great).
• Privacy Policy | Cookies | Terms and Conditions: Improvements needed.
Comments for Teodor
• Footer: We need a footer like TabletNest.
• Mobile Design: Ensure mobile design is similar to TabletNest.
• Social Media and Blogs: Integration needed.
• Email/Marketing List Sign-Up: Implement a sign-up option for patients/visitors.
• Google Reviews: Integrate Google reviews.
• Clinic Videos and Pictures: Include multimedia content.
• Keyword Optimization: Content will be rephrased for keyword optimization (keywords list provided).
• Keywords: I will ask that certain keywords [e.g. from blog] to link certain website page automatically
• DosaTrak Logo: Include DosaTrak logo at the bottom.
• Online Appointment Dropdown: Add dropdown options for different appointment types.
Please proceed with the necessary updates and preparations. Once you have the revised design ready in Figma, kindly send it over for approval.
We currently use the BrookVale Part with Vector and Tag line as the logo for both our Clinic and Pharmacy businesses. However, we have several design considerations and requests:

Banner Designs: What will each banner look like?

Other Pages: How will the other pages appear?

Header and Footer: The current designs for the header and footer are not satisfactory.

Text Placement and Font: We need improved text placement and a better font choice.

Team Members' Pictures: Use actual pictures of our team members.

Logos for Specific Services: Please update the logo/Vector for services such as Chronic Complex Care and Diagnostic Investigations.

Location-Based Pages: We need separate pages for the Pharmacy and Clinic, with links specific to each city—Surrey and White Rock.
Looking forward to seeing the improvements!

• design ready in Figma

```html
<!DOCTYPE html>
<html lang="en">
<head>
<meta charset="utf-8">
<title>BrookVale Care – Medical Clinic &amp; Pharmacy</title>
<link href="https://fonts.googleapis.com/css2?family=Montserrat:wght@600;700;800&family=Poppins:wght@400;500;600;700&display=swap" rel="stylesheet">
<style>
:root{
  --red:#d3222a;
  --green:#22a14b;
  --navy:#2c2f7c;
  --blue:#3d42a2;
  --blue-dark:#363b94;
  --pink:#f8dfe3;
  --pink-soft:#fbe9ec;
  --grey-bg:#f2f2f6;
  --text:#4b4b57;
  --muted:#7a7a86;
  --white:#fff;
}
*{box-sizing:border-box;margin:0;padding:0}
html,body{width:1200px;height:5106px;overflow:hidden}
body{font-family:"Poppins",sans-serif;color:var(--text);background:var(--white);font-size:12px}
h1,h2,h3,h4{font-family:"Montserrat",sans-serif}
section,header,footer,div{position:relative}
.abs{position:absolute}
.btn{display:inline-flex;align-items:center;justify-content:center;font-family:"Poppins",sans-serif;font-weight:600;font-size:10px;letter-spacing:.3px;border-radius:20px;text-transform:uppercase}
.btn-red{background:var(--red);color:#fff}
.btn-green{background:var(--green);color:#fff}
.ph{background:linear-gradient(135deg,#cfd6e4,#eef0f5)}

/* top bar */
.topbar{height:66px;background:#f7f7f9;display:flex;align-items:center;justify-content:center;gap:18px;font-size:10px}
.topbar .flag{width:12px;height:8px;background:var(--red);display:inline-block;margin-right:6px}
.topbar .btn{border:1.5px solid var(--navy);color:var(--navy);height:22px;padding:0 14px;font-size:8.5px}

/* nav */
.nav{height:72px;display:flex;align-items:center;padding:0 100px;border-bottom:1px solid #eee}
.logo{display:flex;align-items:center;gap:8px}
.logo .mark{width:22px;height:22px;background:var(--red)}
.logo span{font-family:"Montserrat",sans-serif;font-weight:800;font-size:19px;color:var(--red)}
.menu{display:flex;gap:29px;margin-left:auto;margin-right:30px}
.menu a{font-size:10.5px;color:var(--navy);text-decoration:none;font-weight:500}
.menu a.active{color:var(--red)}
.nav .btn{height:32px;padding:0 22px}

/* hero */
.hero{height:506px;display:flex}
.hero-copy{width:571px;background:var(--pink);position:relative}
.hero-frame{position:absolute;left:128px;top:48px;width:400px;height:338px;border-top:1.5px solid var(--red);border-left:1.5px solid var(--red)}
.hero-frame:after{content:"";position:absolute;right:0;top:-20px;height:350px;border-right:1.5px solid var(--red)}
.hero-frame:before{content:"";position:absolute;left:-20px;bottom:0;width:430px;border-bottom:1.5px solid var(--red)}
.hero h1{position:absolute;left:171px;top:92px;line-height:1.02}
.hero h1 .l1{display:block;font-size:35px;color:var(--navy);font-weight:800}
.hero h1 .l2{display:block;font-size:49px;color:var(--green);font-weight:800}
.hero p{position:absolute;left:171px;top:252px;font-size:18px;line-height:1.4;color:#333;width:300px}
.hero .btn{position:absolute;left:171px;top:322px;height:32px;padding:0 22px}
.dots{position:absolute;left:0;right:0;top:446px;display:flex;justify-content:center;gap:8px}
.dots i{width:8px;height:8px;border-radius:50%;background:#fff}
.dots i.on{background:var(--red)}
.hero-media{flex:1;background:linear-gradient(120deg,#c9b8a8,#e6e2dc 45%,#b9c4cf)}
.play{position:absolute;left:-22px;top:213px;width:46px;height:46px;border-radius:50%;background:var(--red);border:3px solid #fff;display:flex;align-items:center;justify-content:center}

/* members */
.members{height:149px;display:flex;border-bottom:1px solid #eee}
.members .col{width:50%;padding:42px 0 0 104px}
.members .col+.col{padding-left:148px;border-left:1px solid #ddd;margin:20px 0}
.members .col+.col h4{margin-top:-20px}
.members h4{font-size:11px;color:#222;font-weight:700;margin-bottom:14px}
.badges{display:flex;gap:30px;align-items:center}
.badge{width:70px;height:28px;border-radius:4px;background:#e3e5ee}
.badge.round{width:30px;border-radius:50%;background:#f4d3d6}
.badge.sm{width:56px;height:24px}

/* services */
.services{height:714px;background:var(--grey-bg);text-align:center}
.sec-title{font-size:27px;font-weight:800;color:#16163a}
.services .sec-title{padding-top:62px}
.sub{font-size:13px;color:#444;margin-top:8px}
.services .lead{width:780px;margin:60px auto 0;font-size:13.5px;line-height:1.65;color:#444}
.cards{position:absolute;left:100px;top:304px;display:flex;gap:19px}
.scard{width:236px;height:342px;background:#fff;border-radius:6px;text-align:left;padding:8px 8px 0}
.scard .img{height:160px;border-radius:3px}
.scard .ico{position:absolute;left:18px;top:146px;width:38px;height:38px;border-radius:50%;background:var(--green);border:3px solid #fff}
.scard h3{font-family:"Poppins",sans-serif;font-size:11px;font-weight:600;color:#222;margin:38px 6px 8px}
.scard p{font-size:9.5px;line-height:1.5;margin:0 6px;color:#666}
.scard.featured{background:var(--blue)}
.scard.featured h3,.scard.featured p{color:#fff}
.arrow{position:absolute;width:30px;height:30px;border-radius:50%;border:1.5px solid var(--navy);display:flex;align-items:center;justify-content:center}

/* about */
.about{height:883px}
.pill{display:inline-flex;align-items:center;gap:6px;height:26px;padding:0 14px;border-radius:14px;background:var(--red);color:#fff;font-size:10px;font-weight:600}
.pill i{width:10px;height:10px;border-radius:50%;background:#fff}
.about > .pill{position:absolute;left:100px;top:89px}
.about > .about-title{position:absolute;left:100px;top:126px;width:470px;font-size:25px;line-height:1.32;color:var(--navy);font-weight:800}
.about > .intro{position:absolute;left:100px;top:268px;width:440px;font-size:13px;line-height:1.5;color:#333}
.about > .body{position:absolute;left:100px;top:332px;width:440px;font-size:10.5px;line-height:1.75;color:#555}
.about > .btn{position:absolute;left:100px;top:432px;height:28px;padding:0 18px}
.about-media{position:absolute;left:638px;top:85px;width:432px;height:351px;background:linear-gradient(135deg,#dfe5ec,#f3f3f3 50%,#c9d3de)}
.about-frame-v{position:absolute;top:60px;height:405px;border-left:1.5px solid var(--red)}
.about-frame-h{position:absolute;height:0;border-top:1.5px solid var(--red)}
.mission{position:absolute;left:100px;top:531px;width:1000px;height:282px;background:linear-gradient(100deg,var(--blue),#4c50ad);border-radius:8px;text-align:center;color:#fff;padding-top:76px}
.mission h2{position:static;font-size:40px;font-weight:800;letter-spacing:.5px;line-height:1.2;color:#fff}
.mission p{width:640px;margin:18px auto 0;font-size:15px;line-height:1.65}

/* testimonials */
.reviews{height:525px;background:linear-gradient(180deg,#eef0f5,#f6f6f9)}
.reviews h2{position:absolute;left:100px;top:56px;font-size:24px;font-weight:800;color:var(--navy)}
.reviews .rule{position:absolute;left:100px;top:104px;width:80px;border-top:1.5px solid var(--navy)}
.rating{position:absolute;left:842px;top:44px;display:flex;gap:12px}
.rating .av{width:46px;height:46px;border-radius:50%;background:#c8ccd8}
.rating b{display:block;font-size:9.5px;color:#222;font-weight:600;line-height:1.4}
.rating small{font-size:8.5px;color:#777}
.stars{color:#f2a91e;letter-spacing:1px}
.rcards{position:absolute;left:100px;top:168px;display:flex;gap:20px}
.rcard{width:236px;height:250px;background:#fff;border-radius:6px;text-align:center;padding:26px 22px 0}
.rcard .q{font-family:"Montserrat",sans-serif;font-size:38px;line-height:.8;color:var(--navy);font-weight:800}
.rcard .stars{font-size:12px;margin:8px 0 12px;color:var(--red)}
.rcard p{font-size:9.5px;line-height:1.55;color:#666;height:86px}
.rcard p b{color:var(--navy);font-size:8px}
.who{display:flex;align-items:center;gap:10px;text-align:left;justify-content:center;margin-top:10px}
.who i{width:30px;height:30px;border-radius:50%;background:#cfd3dc}
.who i.g{background:var(--green)}
.who b{display:block;font-size:10px;color:#222;font-weight:600}
.who span{font-size:9px;color:#888}
.pager{position:absolute;left:0;right:0;top:456px;display:flex;justify-content:center;align-items:center;gap:8px}
.pager i{width:8px;height:8px;border-radius:50%;background:#c3c6d8}
.pager i.on{background:var(--navy)}

/* team */
.team{height:545px;text-align:center}
.team .sec-title{padding-top:60px;color:var(--navy)}
.team .rule{width:40px;border-top:1.5px solid #bbb;margin:18px auto 0}
.members-row{position:absolute;left:95px;top:208px;display:flex;gap:28px}
.member{width:182px}
.hex{width:182px;height:220px;clip-path:polygon(50% 0,100% 25%,100% 75%,50% 100%,0 75%,0 25%);background:linear-gradient(160deg,#b89a82,#e7ddd3)}
.member b{display:block;margin-top:14px;font-size:10px;font-weight:600;color:#222}
.member span{font-size:8px;color:#666;font-weight:500}

/* resources */
.resources{height:655px;text-align:center}
.resources .sec-title{padding-top:54px;color:var(--navy)}
.rescards{position:absolute;left:100px;top:163px;display:flex;gap:24px}
.rescard{width:317px;height:363px;background:#fff;border:1px solid #eee;border-radius:4px;text-align:left}
.rescard .img{height:170px}
.rescard h3{font-family:"Poppins",sans-serif;font-size:11.5px;font-weight:600;color:var(--navy);line-height:1.4;margin:26px 24px 10px}
.rescard p{font-size:9px;line-height:1.5;color:#777;margin:0 24px 12px}
.rescard .btn{margin-left:24px;height:22px;padding:0 14px;font-size:8px}
.rescard.featured{background:var(--blue)}
.rescard.featured h3,.rescard.featured p{color:#fff}
.resources .all{position:absolute;left:542px;top:575px;width:154px;height:34px;border:1.5px solid var(--red);color:var(--red);font-size:9.5px;border-radius:18px;display:flex;align-items:center;justify-content:center;font-weight:600}

/* faq */
.faq{height:426px;background:var(--pink-soft)}
.faq .eyebrow{position:absolute;left:100px;top:56px;color:var(--red);font-weight:600;font-size:15px}
.faq h2{position:absolute;left:100px;top:84px;font-family:"Poppins",sans-serif;font-size:30px;font-weight:700;color:var(--navy);line-height:1.25}
.faq .intro{position:absolute;left:100px;top:174px;width:430px;font-size:12.5px;line-height:1.5;color:#444}
.callcard{position:absolute;left:104px;top:244px;width:294px;height:96px;background:#fff;border-radius:10px;display:flex;align-items:center;padding:0 24px;gap:22px}
.callcard small{display:block;font-size:9px;color:#444}
.callcard b{display:block;font-size:11px;color:var(--navy);margin-top:6px;font-weight:600}
.callcard strong{display:block;font-size:19px;color:var(--red);font-weight:700}
.acc{position:absolute;left:590px;top:44px;width:510px}
.acc .open h4{font-family:"Poppins",sans-serif;color:var(--red);font-size:12px;font-weight:600}
.acc .open p{font-size:10.5px;color:#555;line-height:1.55;margin-top:12px;width:440px}
.acc .item{display:flex;justify-content:space-between;align-items:center;height:46px;font-size:11.5px;color:#222;font-weight:500}
.acc .open{padding-bottom:34px}

/* footer */
.site-footer{height:466px;background:linear-gradient(180deg,var(--blue-dark),#3d42a2);color:#fff}
.site-footer .logo{position:absolute;left:100px;top:56px}
.site-footer .logo span{color:#fff;font-size:24px}
.site-footer .logo .mark{background:#fff}
.newsletter{position:absolute;left:100px;top:144px;width:302px}
.newsletter h4{font-size:11px;font-weight:700;margin-bottom:10px}
.field{height:34px;border-radius:18px;background:#fff;color:#777;font-size:9.5px;display:flex;align-items:center;padding-left:20px;margin-bottom:12px}
.newsletter .btn{width:100%;height:36px;font-size:14px;border-radius:18px}
.fcol{position:absolute;top:50px;width:170px;font-size:8.5px;line-height:1.5;color:#e4e5f5}
.fcol h4{font-size:10.5px;color:#fff;font-weight:700;line-height:1.35;margin-bottom:12px}
.fcol p{margin-bottom:9px}
.fmenu{position:absolute;left:108px;top:380px;font-size:9px}
.fmenu h4{font-size:11px;font-weight:700;margin-bottom:12px}
.fmenu nav{display:flex;gap:10px;color:#e4e5f5}
.bottom{height:99px;display:flex;align-items:center;padding:0 100px}
.bottom .brand{display:flex;align-items:center;gap:8px}
.bottom .brand i{width:32px;height:32px;border-radius:50%;border:3px solid var(--navy)}
.bottom .brand span{font-size:22px;font-weight:600;color:var(--navy)}
.follow{margin-left:240px;display:flex;align-items:center;gap:6px;font-size:9.5px;font-weight:700;color:var(--navy)}
.follow b{margin-right:10px}
.follow i{width:26px;height:26px;border-radius:50%;background:var(--navy)}
.legal{margin-left:auto;text-align:left;font-size:9px;line-height:1.9;color:var(--navy)}
</style>
</head>
<body>

<div class="topbar">
  <span><i class="flag"></i>Proudly Canadian and locally owned and operated. Our doctors and nurse practitioners are now accepting new patients.</span>
  <a class="btn">Download Intake Forms</a>
</div>

<header class="nav">
  <div class="logo"><i class="mark"></i><span>BrookVale Care</span></div>
  <nav class="menu">
    <a class="active">MEDICAL CLINIC</a><a>PHARMACY</a><a>HOME MONITORING</a><a>HOME HEALTHCARE</a><a>CONTACT US</a><a>RESOURCES</a>
  </nav>
  <a class="btn btn-green">Book Appointment</a>
</header>

<section class="hero">
  <div class="hero-copy">
    <div class="hero-frame"></div>
    <h1><span class="l1">NEW FAMILY</span><span class="l2">PHYSICIAN<br>NEEDED</span></h1>
    <p>We Invite Doctors who are interested joining our team!</p>
    <a class="btn btn-red">Join Our Team</a>
    <div class="dots"><i class="on"></i><i></i><i></i><i></i><i></i></div>
  </div>
  <div class="hero-media" role="img" aria-label="Doctor giving a high five to a young boy sitting with his father">
    <div class="play"><svg width="14" height="16" viewBox="0 0 14 16"><path d="M2 1l11 7-11 7z" fill="#fff"/></svg></div>
  </div>
</section>

<section class="members">
  <div class="col">
    <h4>MEMBER OF</h4>
    <div class="badges"><i class="badge round"></i><i class="badge"></i><i class="badge"></i></div>
  </div>
  <div class="col">
    <h4>LICENSED BY</h4>
    <div class="badges"><i class="badge sm"></i><i class="badge"></i><i class="badge sm"></i><i class="badge sm"></i></div>
  </div>
</section>

<section class="services">
  <h2 class="sec-title">OUR SERVICES</h2>
  <p class="sub">Convenient, Quality Care in Surrey and White Rock</p>
  <p class="lead">At our walk-in clinic and medical clinic in Surrey and White Rock, we offer a wide range of healthcare services to meet the diverse needs of our community. Whether you're looking for urgent care, routine check-ups, or specialized treatment, we provide accessible, affordable healthcare in Surrey and White Rock.</p>
  <div class="arrow" style="left:40px;top:478px"><svg width="10" height="10" viewBox="0 0 10 10"><path d="M7 1L3 5l4 4" stroke="#2c2f7c" stroke-width="1.5" fill="none"/></svg></div>
  <div class="arrow" style="left:1127px;top:478px"><svg width="10" height="10" viewBox="0 0 10 10"><path d="M3 1l4 4-4 4" stroke="#2c2f7c" stroke-width="1.5" fill="none"/></svg></div>
  <div class="cards">
    <article class="scard featured">
      <div class="img" role="img" aria-label="Diagnostic screen showing a human body scan" style="background:linear-gradient(135deg,#1f3b73,#4f8fc7)"></div>
      <i class="ico"></i>
      <h3>DIAGNOSTIC INVESTIGATION</h3>
      <p>Our medical clinic near me provides a wide range of diagnostic tests and procedures to identify potential issues, ensuring that patients receive timely care when symptoms arise or other tests indicate a need for further investigation.</p>
    </article>
    <article class="scard">
      <div class="img ph" role="img" aria-label="Medical screening monitor in a clinic"></div>
      <i class="ico"></i>
      <h3>SCREENING EXAMS</h3>
      <p>We provide various health screenings, including PAP tests, manual breast exams, prostate exams, colon cancer prevention, and other early detection services to ensure you stay on top of your health.</p>
    </article>
    <article class="scard">
      <div class="img ph" role="img" aria-label="Doctor speaking with a patient at the walk-in clinic"></div>
      <i class="ico"></i>
      <h3>WALK-IN CLINIC SURREY</h3>
      <p>Our medical clinic Surrey offers top-quality, convenient care for all your healthcare needs with an appointment. Visit us for immediate attention and professional service.</p>
    </article>
    <article class="scard">
      <div class="img ph" role="img" aria-label="Pharmacist working among pharmacy shelves"></div>
      <i class="ico"></i>
      <h3>ONSITE PHARMACY</h3>
      <p>Our patients enjoy the convenience of an onsite pharmacy that provides prescription delivery, medication reviews, vaccinations, blister packing, and same-day delivery pharmacy services.</p>
    </article>
  </div>
</section>

<section class="about">
  <span class="pill"><i></i>ABOUT US</span>
  <h2 class="about-title">WE'RE AN ESTABLISHED, FORWARD-THINKING FAMILY PRACTICE IN WHITE ROCK/SOUTH SURREY.</h2>
  <p class="intro">We're proud to provide top-notch healthcare services at BrookVale in White Rock.</p>
  <p class="body">We are a trusted family doctor in White Rock and Surrey, committed to offering reliable family doctors in Surrey with a focus on providing convenient medical care in Surrey. Our medical clinic Surrey and walk-in clinic Surrey are equipped with the latest technology and a skilled team to ensure exceptional care in a safe and supportive environment.</p>
  <a class="btn btn-red">Read More</a>
  <div class="about-frame-v" style="left:634px"></div>
  <div class="about-frame-v" style="left:1084px"></div>
  <div class="about-frame-h" style="left:620px;top:80px;width:478px"></div>
  <div class="about-frame-h" style="left:620px;top:440px;width:478px"></div>
  <div class="about-media" role="img" aria-label="Smiling patient talking with a doctor holding a tablet"></div>
  <div class="mission">
    <h2>MISSION STATEMENT</h2>
    <p>Our mission is to be the best walk-in clinic in Surrey and a top-rated medical clinic in Surrey, leading the way in innovation and patient care. We aim to provide affordable healthcare in Surrey that is empathetic, efficient, and accessible to all.</p>
  </div>
</section>

<section class="reviews">
  <h2>WHAT OUR CLIENT SAYS ABOUT US</h2>
  <div class="rule"></div>
  <div class="rating">
    <i class="av"></i>
    <div><b>BrookVale Pharmacy &amp; Vaccine Clinic -<br>White Rock/South Surrey</b><small><span class="stars" style="color:#e08a1e">4.9 ★★★★★</span> &nbsp;Based on 159 reviews</small></div>
  </div>
  <div class="rcards">
    <article class="rcard"><div class="q">“</div><div class="stars">★★★★★</div><p>Excellent- thank goodness for this service! It has saved us several hours waiting in emergency for something that was handled quickly and efficiently by the doctor on call.</p><div class="who"><i class="g"></i><div><b>Mirela Dask</b><span>8 months ago</span></div></div></article>
    <article class="rcard"><div class="q">“</div><div class="stars">★★★★★</div><p>WhiteRock BrookVale Pharmacy is amazing! Their free delivery for prescriptions has been a lifesaver for us. We got flu shots and booster shots there easily, and the fees were really reasonable. <b>MORE</b></p><div class="who"><i></i><div><b>Mirela Dask</b><span>8 months ago</span></div></div></article>
    <article class="rcard"><div class="q">“</div><div class="stars">★★★★★</div><p>I am very pleased and happy with the level of care I have experienced at this clinic. The doctor and her team are great to deal with. Their online appointment booking system is awesome! <b>MORE</b></p><div class="who"><i></i><div><b>Mirela Dask</b><span>8 months ago</span></div></div></article>
    <article class="rcard"><div class="q">“</div><div class="stars">★★★★★</div><p>Very satisfied with the overall care by the doctor and the pharmacy, thank you for the quick scheduling and response.</p><div class="who"><i></i><div><b>Mirela Dask</b><span>8 months ago</span></div></div></article>
  </div>
  <div class="pager">
    <svg width="12" height="14" viewBox="0 0 12 14"><path d="M9 1L3 7l6 6" stroke="#2c2f7c" stroke-width="1.5" fill="none"/></svg>
    <i class="on"></i><i></i><i></i><i></i><i></i>
    <svg width="12" height="14" viewBox="0 0 12 14"><path d="M3 1l6 6-6 6" stroke="#2c2f7c" stroke-width="1.5" fill="none"/></svg>
  </div>
</section>

<section class="team">
  <h2 class="sec-title">OUR TEAM</h2>
  <p class="sub" style="font-size:15px">Healing minds with compassionate hearts.</p>
  <div class="rule"></div>
  <svg class="abs" style="left:32px;top:302px" width="14" height="24" viewBox="0 0 14 24"><path d="M12 2L2 12l10 10" stroke="#2c2f7c" stroke-width="2" fill="none"/></svg>
  <svg class="abs" style="left:1140px;top:302px" width="14" height="24" viewBox="0 0 14 24"><path d="M2 2l10 10-10 10" stroke="#2c2f7c" stroke-width="2" fill="none"/></svg>
  <div class="members-row">
    <div class="member"><div class="hex" role="img" aria-label="Portrait of the medical director"></div><b>DR MARLOW PENNICK</b><span>MEDICAL DIRECTOR</span></div>
    <div class="member"><div class="hex" role="img" aria-label="Portrait of the medical director"></div><b>DR IDRIS VALCOURT</b><span>MEDICAL DIRECTOR</span></div>
    <div class="member"><div class="hex" role="img" aria-label="Portrait of a family physician"></div><b>DR. NESSA O. LARKWELL, MD</b><span>FAMILY PHYSICIAN [JOINING SOON]</span></div>
    <div class="member"><div class="hex" role="img" aria-label="Portrait of a family physician"></div><b>DR. KELLAN T. RUVIO, MD</b><span>FAMILY PHYSICIAN [JOINING SOON]</span></div>
    <div class="member"><div class="hex" role="img" aria-label="Portrait of a family physician"></div><b>DR. ORLA QUENNET, MD</b><span>FAMILY PHYSICIAN [JOINING SOON]</span></div>
  </div>
</section>

<section class="resources">
  <h2 class="sec-title">RESOURCES</h2>
  <p class="sub" style="font-size:15px">Explore the latest news and resources.</p>
  <div class="rescards">
    <article class="rescard featured">
      <div class="img ph" role="img" aria-label="Doctor consulting with an older patient"></div>
      <h3>WHAT TO DO IF YOU DON'T HAVE A FAMILY DOCTOR IN WHITE ROCK, SOUTH SURREY, AND SURREY</h3>
      <p>Finding a family doctor in White Rock, South Surrey, or Surrey can be challenging, especially if you're new to the area or your current doctor has retired.</p>
      <a class="btn btn-red">Read More</a>
    </article>
    <article class="rescard">
      <div class="img ph" role="img" aria-label="Caregiver holding hands with a senior patient"></div>
      <h3>ENHANCING PATIENT CARE WITH BROOKVALE PHARMACY'S HOME MONITORING PROGRAM</h3>
      <p>Welcome to BrookVale Pharmacy – White Rock! We understand how crucial accessible healthcare is, and we're here to assist with your medication needs.</p>
      <a class="btn btn-red">Read More</a>
    </article>
    <article class="rescard">
      <div class="img" role="img" aria-label="Medication pen and product box" style="background:linear-gradient(135deg,#f4f4f7,#e4e2ee)"></div>
      <h3>GLYVORA: HOW BROOKVALE PHARMACY CAN HELP YOU WITH YOUR PRESCRIPTION NEEDS</h3>
      <p>Welcome to BrookVale Pharmacy – White Rock! We understand how crucial accessible healthcare is, and we're here to assist with your medication needs.</p>
      <a class="btn btn-red">Read More</a>
    </article>
  </div>
  <a class="all">VIEW ALL RESOURCES</a>
</section>

<section class="faq">
  <p class="eyebrow">Frequently Asked Questions</p>
  <h2>Helping you understand<br>healthcare</h2>
  <p class="intro">Here to make your experience as seamless as possible - explore answers to common questions about our services, policies, and patient care.</p>
  <div class="callcard">
    <svg width="30" height="30" viewBox="0 0 24 24"><path d="M6.6 10.8a15 15 0 006.6 6.6l2.2-2.2a1 1 0 011-.25 11.4 11.4 0 003.6.57 1 1 0 011 1V20a1 1 0 01-1 1A17 17 0 013 4a1 1 0 011-1h3.5a1 1 0 011 1c0 1.250.2 2.450.57 3.6a1 1 0 01-.25 1z" fill="none" stroke="#d3222a" stroke-width="1.5"/></svg>
    <div><small>We always take care of your smile</small><b>24/7 Emergency</b><strong>604-555-0148</strong></div>
  </div>
  <div class="acc">
    <div class="open">
      <div style="display:flex;justify-content:space-between"><h4>Helping you understand healthcare</h4><svg width="12" height="8" viewBox="0 0 12 8"><path d="M1 7l5-5 5 5" stroke="#d3222a" stroke-width="1.5" fill="none"/></svg></div>
      <p>Here to make your experience as seamless as possible-explore answers to common questions about our services, policies, and patient care.</p>
    </div>
    <div class="item">How do I schedule an appointment?<svg width="12" height="8" viewBox="0 0 12 8"><path d="M1 1l5 5 5-5" stroke="#333" stroke-width="1.5" fill="none"/></svg></div>
    <div class="item">What insurance plans do you accept?<svg width="12" height="8" viewBox="0 0 12 8"><path d="M1 1l5 5 5-5" stroke="#333" stroke-width="1.5" fill="none"/></svg></div>
    <div class="item">Can I get a prescription refill without an appointment?<svg width="12" height="8" viewBox="0 0 12 8"><path d="M1 1l5 5 5-5" stroke="#333" stroke-width="1.5" fill="none"/></svg></div>
    <div class="item">What should I expect during my first visit?<svg width="12" height="8" viewBox="0 0 12 8"><path d="M1 1l5 5 5-5" stroke="#333" stroke-width="1.5" fill="none"/></svg></div>
    <div class="item">How are treatment plans customized for individual needs?<svg width="12" height="8" viewBox="0 0 12 8"><path d="M1 1l5 5 5-5" stroke="#333" stroke-width="1.5" fill="none"/></svg></div>
  </div>
</section>

<footer class="site-footer">
  <div class="logo"><i class="mark"></i><span>BrookVale Care</span></div>
  <div class="newsletter">
    <h4>NEWSLETTER SUBSCRIBE</h4>
    <div class="field">FULL NAME</div>
    <div class="field">EMAIL ID</div>
    <a class="btn btn-green">Subscribe</a>
  </div>
  <div class="fcol" style="left:466px">
    <h4>BROOKVALE MEDICAL CLINIC – WHITE ROCK</h4>
    <p>4-1200 Alder Lane<br>White Rock, BC V4B 0A1</p>
    <p>Monday – Friday<br>09:00 AM – 05:00 PM</p>
    <p>Saturday, Sunday and Statutory<br>Holiday – Closed</p>
    <p>Online Services</p>
    <p>Monday to Sunday<br>09:00 AM – 06:30 PM</p>
    <p>info@brookvalecare.ca</p>
    <p>Phone: +1 (604) 555-0193</p>
    <p>Fax: +1 (604) 555-0192</p>
  </div>
  <div class="fcol" style="left:704px">
    <h4>BROOKVALE PHARMACY – WHITE ROCK</h4>
    <p>4-1200 Alder Lane<br>White Rock, BC V4B 0A1</p>
    <p>Monday – Friday<br>09:00 AM – 06:30 PM</p>
    <p>Saturday – 10:00 AM – 03:30 PM<br>Sunday and Statutory Holiday</p>
    <p>10:00 AM – 02:00 PM</p>
    <p>We offer Free Delivery</p>
    <p>Weekdays – Same Day Free<br>Delivery(On orders before 04:00 PM)</p>
    <p>Weekends – Next Day Free Delivery</p>
    <p>rx@brookvalecare.ca</p>
    <p>Phone: +1 (604) 555-0190</p>
    <p>Fax: +1 (604) 555-0191</p>
  </div>
  <div class="fcol" style="left:944px">
    <h4>BROOKVALE MEDICAL CLINIC – SURREY</h4>
    <p>#108-109 15220 Juniper Ave<br>Surrey BC, V3S 0A2</p>
    <p>Monday – Friday<br>9:00AM – 8:30PM</p>
    <p>medical@brookvalecare.ca</p>
    <p>Phone: +1 (604) 555-0166</p>
    <p>Fax: +1 (604) 555-0167</p>
    <h4 style="margin-top:26px">BROOKVALE PHARMACY – SURREY</h4>
    <p>#107 15220 Juniper Ave<br>Surrey BC, V3S 0A2</p>
    <p>Monday – Friday<br>9:00AM – 8:30PM</p>
    <p>pharmacy@brookvalecare.ca</p>
    <p>Phone: +1 (604) 555-0164</p>
    <p>Fax: +1 (604) 555-0165</p>
  </div>
  <div class="fmenu">
    <h4>MENU</h4>
    <nav><span>Medical Clinic</span>|<span>Pharmacy</span>|<span>Home Monitoring</span>|<span>Home Healthcare</span>|<span>Contact Us</span>|<span>Resources</span>|<span>Join Our Team</span></nav>
  </div>
</footer>

<div class="bottom">
  <div class="brand"><i></i><span>DosaTrak</span></div>
  <div class="follow"><b>FOLLOW US</b><i></i><i></i><i></i><i></i><i></i></div>
  <div class="legal">Privacy Policy | Cookies | Terms and Conditions<br>Copyright © 2025 BrookVale Medical All rights reserved.</div>
</div>

</body>
</html>
```